Plumbing website that stands out

Seo optimized, mobile friendly, easily editable word press Plumbing website with RatedLocal Reviews widget. And widget of revolving photos of completed work. Contact page and services page, about page. Will provide, “About” content. And photos Need all other content written.
Services include:
Water heater replacement
Tankless water heater installation
Kitchen and bath remodel
Drain cleaning and clog removal
Leak repair
Faucet repair and replacement

I will be adding services and photos of recent completed projects as time goes on.

```html
<!DOCTYPE html>
<html lang="en">
<head>
<meta charset="utf-8">
<title>Clearline Plumbing — Trusted Emergency Water Plumbing</title>
<link href="https://fonts.googleapis.com/css2?family=Cinzel:wght@400;600;700&family=Montserrat:ital,wght@0,400;0,500;0,600;0,700;1,400&display=swap" rel="stylesheet">
<style>
  :root{
    --navy:#0c3f7a;
    --hero:#0f4d8c;
    --teal:#2ba8b9;
    --teal-band:#14818f;
    --teal-light:#4cc0cf;
    --ink:#1e2d3d;
    --muted:#5b6673;
    --footer:#0a2c5a;
    --light:#f1f4f8;
    --white:#ffffff;
    --star:#f5b400;
  }
  *{margin:0;padding:0;box-sizing:border-box}
  html,body{width:1200px;height:4222px;overflow:hidden}
  body{position:relative;background:var(--white);font-family:"Montserrat",sans-serif;color:var(--ink)}
  .abs{position:absolute}
  .img-fill{position:absolute}

  /* header */
  .site-header{position:absolute;left:0;top:0;width:1200px;height:94px;background:var(--white);z-index:3}
  .brand-box{position:absolute;left:79px;top:0;width:196px;height:112px;background:var(--white);border-radius:0 0 6px 6px;z-index:5;display:flex;flex-direction:column;align-items:center;justify-content:center;box-shadow:0 2px 6px rgba(0,0,0,.08)}
  .brand-box .mark{width:34px;height:34px;background:var(--navy);border-radius:4px;margin-bottom:8px}
  .brand-name{font-family:"Cinzel",serif;font-weight:600;color:var(--navy);font-size:17px;letter-spacing:2px;text-align:center;line-height:1.2}
  .top-locate{position:absolute;left:549px;top:13px;font-size:11px;font-weight:600;color:var(--navy);display:flex;align-items:center;gap:6px}
  .top-phone{position:absolute;left:688px;top:0;width:205px;height:36px;background:var(--teal);color:#fff;font-weight:600;font-size:16px;display:flex;align-items:center;justify-content:center;gap:8px;border-radius:0 0 0 16px}
  .top-request{position:absolute;left:893px;top:0;width:197px;height:36px;background:var(--navy);color:#fff;font-weight:600;font-size:13px;display:flex;align-items:center;justify-content:center;border-radius:0 0 16px 0}
  .main-nav a{position:absolute;top:58px;font-size:12px;font-weight:500;color:var(--ink);text-decoration:none}
  .main-nav a.active{color:var(--teal)}

  /* hero */
  .hero{position:absolute;left:0;top:94px;width:1200px;height:540px}
  .hero-tag{left:88px;top:200px;color:#fff;font-size:13px;font-weight:600}
  .hero-tag span{color:var(--teal-light)}
  .hero-title{left:88px;top:230px;color:#fff;font-family:"Cinzel",serif;font-weight:700;font-size:39px;line-height:49px;z-index:2}
  .hero-rule{left:88px;top:351px;width:392px;height:1px;background:rgba(255,255,255,.6)}
  .hero-rule::before{content:"";position:absolute;left:0;top:-4px;width:8px;height:8px;border-radius:50%;background:#fff}
  .hero-text{left:88px;top:373px;width:400px;color:#fff;font-size:12.5px;line-height:21px}
  .btn{position:absolute;display:flex;align-items:center;justify-content:center;color:#fff;font-weight:600;text-transform:uppercase;letter-spacing:.3px}
  .btn-hero{left:87px;top:459px;width:197px;height:41px;background:var(--teal);font-size:13px;border-radius:2px}

  .rating-card{left:380px;top:541px;width:443px;height:152px;background:#fff;border-radius:6px;box-shadow:0 6px 20px rgba(0,0,0,.15);z-index:4}
  .rating-top{position:absolute;left:7px;top:10px;width:429px;height:60px;background:var(--navy);border-radius:6px;color:#fff}
  .rating-top .score{position:absolute;left:25px;top:14px;font-size:26px;font-weight:700}
  .rating-top .stars{position:absolute;left:86px;top:17px;font-size:22px;letter-spacing:2px}
  .rating-top .divider{position:absolute;left:232px;top:12px;width:1px;height:36px;background:rgba(255,255,255,.4)}
  .rating-top .count{position:absolute;left:260px;top:14px;font-size:26px;font-weight:700}
  .rating-top .count sup{font-size:14px}
  .rating-top .label{position:absolute;left:337px;top:18px;font-size:10px;font-weight:700;line-height:12px}
  .rating-brand{position:absolute;left:34px;top:85px;font-size:22px;font-weight:600;color:var(--navy)}
  .rating-brand small{display:block;font-size:11px;color:var(--muted);font-weight:600}
  .rating-brand small i{color:var(--star);font-style:normal}
  .top-rated{position:absolute;left:247px;top:98px;font-size:10px;color:var(--ink)}
  .avatar{position:absolute;top:91px;width:28px;height:28px;border-radius:50%;border:2px solid #fff}

  /* about */
  .eyebrow{font-size:13px;font-weight:600;letter-spacing:1.5px;color:var(--navy);text-transform:uppercase}
  .about-eyebrow{left:607px;top:789px}
  .about-title{left:605px;top:816px;font-family:"Cinzel",serif;font-weight:400;font-size:32px;line-height:38px;color:var(--ink)}
  .about-bar{left:587px;top:822px;width:4px;height:98px;background:var(--navy)}
  .body-copy{font-size:13px;line-height:25px;color:var(--muted)}
  .about-p1{left:607px;top:946px;width:440px}
  .about-p2{left:607px;top:1070px;width:440px}
  .btn-learn{left:607px;top:1175px;width:134px;height:35px;background:var(--teal);border-radius:18px;font-family:"Cinzel",serif;text-transform:none;font-size:13px}

  /* services */
  .services-wave{position:absolute;left:0;top:1300px}
  .services-head{left:0;width:1200px;text-align:center;color:#fff}
  .svc-eyebrow{top:1403px;font-size:13px;font-weight:600;letter-spacing:.5px}
  .svc-title{top:1428px;font-family:"Cinzel",serif;font-weight:400;font-size:34px;letter-spacing:1px}
  .svc-text{top:1480px;left:370px;width:460px;font-size:11px;line-height:17px}
  .svc-item{position:absolute;top:1567px;width:140px;text-align:center;color:#fff;font-size:10.5px;font-weight:700;line-height:13px}
  .svc-icon{width:66px;height:66px;border-radius:50%;border:2px solid rgba(255,255,255,.85);margin:0 auto 24px;display:flex;align-items:center;justify-content:center}
  .svc-icon.active{background:#fff;border-color:#fff}
  .svc-sep{position:absolute;top:1572px;width:1px;height:100px;background:rgba(255,255,255,.25)}
  .svc-underline{left:197px;top:1700px;width:75px;height:3px;background:var(--teal-light)}
  .svc-detail-title{left:197px;top:1750px;color:#fff;font-size:22px;font-weight:700}
  .svc-detail-sub{left:197px;top:1792px;color:#fff;font-size:11px;font-weight:700;line-height:14px}
  .svc-detail-text{left:197px;top:1838px;width:375px;color:#fff;font-size:10.5px;line-height:21px}
  .btn-svc{left:197px;top:2008px;width:182px;height:39px;background:var(--teal);border:2px solid rgba(255,255,255,.5);font-size:12px}

  /* testimonials */
  .testimonials{left:0;top:2147px;width:1200px;height:517px;background:var(--light)}
  .center{left:0;width:1200px;text-align:center}
  .tst-eyebrow{top:2216px;font-size:13px;font-weight:600;letter-spacing:1.5px;color:var(--teal)}
  .tst-title{top:2242px;font-family:"Cinzel",serif;font-weight:400;font-size:32px;color:var(--ink)}
  .tst-bar{left:341px;top:2250px;width:3px;height:24px;background:var(--teal)}
  .tst-sub{top:2288px;font-size:12px;color:var(--muted)}
  .tcard{position:absolute;top:2341px;width:259px;height:244px;background:#fff;box-shadow:0 4px 14px rgba(0,0,0,.08)}
  .tcard .quote{position:absolute;left:27px;top:22px;font-family:Georgia,serif;font-size:48px;font-weight:700;color:var(--navy);line-height:40px}
  .tcard p{position:absolute;left:27px;top:64px;width:222px;font-size:10px;line-height:20px;color:var(--muted);font-style:italic}
  .tcard .stars{position:absolute;left:27px;top:152px;font-size:13px;color:var(--teal);letter-spacing:2px}
  .tcard .g{position:absolute;left:28px;top:186px;width:34px;height:34px;border-radius:50%;border:5px solid #e3a81d}
  .tcard .name{position:absolute;left:76px;top:188px;font-size:12px;font-weight:600;color:var(--navy)}
  .tcard .role{position:absolute;left:76px;top:207px;font-size:10px;color:var(--muted)}
  .arrow{position:absolute;top:2438px;width:44px;height:44px;border-radius:50%;background:#fff;box-shadow:0 2px 8px rgba(0,0,0,.12);display:flex;align-items:center;justify-content:center}

  /* location */
  .loc-eyebrow{left:144px;top:2740px;font-size:12px;font-weight:600;color:var(--teal)}
  .loc-title{left:144px;top:2762px;font-family:"Cinzel",serif;font-weight:400;font-size:34px;color:var(--ink)}
  .loc-text{left:144px;top:2816px;width:478px;font-size:10.5px;line-height:18px;color:var(--muted);border-left:2px solid var(--teal);padding-left:10px}
  .areas-card{left:144px;top:2896px;width:484px;height:202px;background:#fff;box-shadow:0 4px 16px rgba(0,0,0,.12)}
  .areas-tab{position:absolute;top:13px;height:30px;font-family:"Cinzel",serif;font-size:14px;display:flex;align-items:center;justify-content:center;color:var(--ink)}
  .areas-tab.active{background:var(--navy);color:#fff}
  .area{position:absolute;font-size:10px;color:var(--muted);display:flex;align-items:center;gap:6px}
  .map-circle{left:708px;top:2752px;width:354px;height:354px;border-radius:50%;background:radial-gradient(circle at 45% 55%,#c9dff3 0%,#e8eef0 45%,#f3f1e6 100%)}

  /* contact */
  .contact-bg{left:0;top:3183px;width:1200px;height:384px;background:var(--light)}
  .footer{left:0;top:3567px;width:1200px;height:655px;background:var(--footer)}
  .ct-eyebrow{top:3235px;font-size:12px;font-weight:600;color:var(--teal)}
  .ct-title{top:3258px;font-family:"Cinzel",serif;font-weight:400;font-size:34px;color:var(--ink);letter-spacing:1px}
  .contact-card{left:161px;top:3334px;width:875px;height:415px;background:#fff;box-shadow:0 4px 16px rgba(0,0,0,.08)}
  .ct-heading{left:216px;top:3384px;font-family:"Cinzel",serif;font-weight:400;font-size:23px;color:var(--ink)}
  .ct-lead{left:216px;top:3424px;width:260px;font-size:10px;line-height:16px;color:var(--muted)}
  .ct-icon{position:absolute;left:217px;width:48px;height:48px;border-radius:50%;background:var(--navy);border:3px solid #d7e2ef;display:flex;align-items:center;justify-content:center}
  .ct-label{position:absolute;left:282px;font-family:"Cinzel",serif;font-size:15px;color:var(--ink)}
  .ct-value{position:absolute;left:282px;font-size:10.5px;line-height:16px;color:var(--ink);width:200px}
  .form-box{left:607px;top:3381px;width:370px;height:419px;background:var(--teal)}
  .form-title{position:absolute;left:0;top:36px;width:370px;text-align:center;color:#fff;font-size:21px;font-weight:700}
  .field{position:absolute;left:52px;width:270px;border-bottom:1px solid rgba(255,255,255,.5);color:#fff;font-size:10px;padding-bottom:8px}
  .btn-send{left:661px;top:3736px;width:129px;height:34px;background:#fff;color:var(--teal);font-size:10px;border-radius:2px}

  .foot-brand{left:150px;top:3870px;width:184px;text-align:center}
  .foot-brand .mark{width:30px;height:30px;border-radius:4px;background:#fff;margin:0 auto 10px}
  .foot-brand .brand-name{color:#fff;font-size:18px}
  .foot-about{left:159px;top:3970px;width:200px;color:#fff;font-size:10px;line-height:18px}
  .foot-col h4{font-family:"Cinzel",serif;font-weight:400;color:#fff;font-size:16px;letter-spacing:1px}
  .foot-col h4::after{content:"";display:block;width:34px;height:2px;background:var(--teal);margin-top:8px}
  .foot-col ul{list-style:none;margin-top:14px}
  .foot-col li{color:#fff;font-size:10.5px;line-height:28px}
  .foot-contact li{display:flex;gap:10px;align-items:flex-start;line-height:18px;margin-bottom:14px}
  .copyright{top:4178px;font-size:10px;color:#fff}
</style>
</head>
<body>

<!-- Header -->
<header class="site-header">
  <div class="top-locate">
    <svg width="14" height="14" viewBox="0 0 14 14"><circle cx="7" cy="7" r="7" fill="var(--navy)"/><path d="M7 3a2.5 2.5 0 0 0-2.5 2.5C4.5 7.5 7 10.5 7 10.5s2.5-3 2.5-5A2.5 2.5 0 0 0 7 3z" fill="#fff"/></svg>
    Find a Location
  </div>
  <div class="top-phone">
    <svg width="16" height="16" viewBox="0 0 24 24"><path d="M6.6 10.8a15 15 0 0 0 6.6 6.6l2.2-2.2a1 1 0 0 1 1-.25 11.4 11.4 0 0 0 3.6.57 1 1 0 0 1 1 1V20a1 1 0 0 1-1 1A17 17 0 0 1 3 4a1 1 0 0 1 1-1h3.5a1 1 0 0 1 1 1c0 1.25.2 2.45.57 3.6a1 1 0 0 1-.25 1z" fill="#fff"/></svg>
    010-555-01-234
  </div>
  <div class="top-request">Request Services</div>
  <nav class="main-nav">
    <a class="active" style="left:549px">Home</a>
    <a style="left:635px">About</a>
    <a style="left:721px">Services</a>
    <a style="left:820px">Commercail</a>
    <a style="left:941px">BLog</a>
    <a style="left:1021px">Contact Us</a>
  </nav>
</header>
<div class="brand-box">
  <div class="mark"></div>
  <div class="brand-name">CLEARLINE PLUMBING</div>
</div>

<!-- Hero -->
<section class="hero">
  <svg width="1200" height="540" viewBox="0 0 1200 540" style="position:absolute;left:0;top:0">
    <defs>
      <linearGradient id="heroGrad" x1="0" y1="0" x2="1" y2="1">
        <stop offset="0" stop-color="#0c3f7a"/>
        <stop offset="1" stop-color="#155c9c"/>
      </linearGradient>
    </defs>
    <path d="M0 0H1200V470C1080 440 980 445 860 470 C700 505 560 510 420 500 C250 488 120 530 0 515Z" fill="url(#heroGrad)"/>
  </svg>
</section>
<div class="img-fill" role="img" aria-label="White branded plumbing service van" style="left:620px;top:200px;width:580px;height:275px;background:linear-gradient(180deg,#f4f6f8 0%,#dfe4ea 70%,#2c3440 100%);border-radius:120px 0 40px 40px"></div>
<div class="abs hero-tag">WE GIVE YOU THE <span>BEST VALUE</span> POSSIBLE</div>
<h1 class="abs hero-title">Trusted Emergency<br>Water Plumbing</h1>
<div class="abs hero-rule"></div>
<p class="abs hero-text">Lorem ipsum dolor sit amet, consectetur adipiscing elit, sed do at eiusmod tempor incididunt ut labore et dolore magna aliqua. Ut enim ad minim veniam, quis nostrud exercitation.</p>
<div class="btn btn-hero">Request Services</div>

<div class="abs rating-card">
  <div class="rating-top">
    <div class="score">4.9</div>
    <div class="stars">★★★★★</div>
    <div class="divider"></div>
    <div class="count">860<sup>+</sup></div>
    <div class="label">CUSTOMER<br>REVIEWS</div>
  </div>
  <div class="rating-brand">RatedLocal<small>Reviews <i>★★★★★</i></small></div>
  <div class="top-rated">Top Rated</div>
  <div class="avatar" style="left:314px;background:#c98a5e"></div>
  <div class="avatar" style="left:336px;background:#6d8fb5"></div>
  <div class="avatar" style="left:358px;background:#a76b50"></div>
  <div class="avatar" style="left:380px;background:#3c5f8a"></div>
</div>

<!-- About -->
<div class="img-fill" role="img" aria-label="Plumber in a blue hard hat and safety glasses repairing pipes" style="left:89px;top:774px;width:432px;height:462px;background:linear-gradient(135deg,#c9ced3 0%,#8aa3bf 50%,#2d5a96 100%);border-radius:0 60px 0 60px"></div>
<div class="abs eyebrow about-eyebrow">About Us</div>
<div class="abs about-bar"></div>
<h2 class="abs about-title">Plumbing, Heating,<br>Furnace, Air Conditioning,<br>Drainage Services</h2>
<p class="abs body-copy about-p1">Lorem ipsum dolor sit amet, consectetur adipiscing elit, sed do eiusmod tempor incididunt ut labore et dolore magna aliqua enim ad minim veniam, quis nostrud exercitation ullamco laboris nisi ut aliquip ex ea commodo consequat.</p>
<p class="abs body-copy about-p2">Duis aute irure dolor in reprehenderit in voluptate velit esse cillum dolore eu fugiat nulla pariatur excepteur sint occaecat cupidatat non proident, sunt in culpa qui officia.</p>
<div class="btn btn-learn">Learn More</div>

<!-- Services -->
<svg class="services-wave" width="1200" height="860" viewBox="0 0 1200 860">
  <path d="M0 35C150 0 300 25 450 30 C650 38 800 5 980 20 C1080 28 1150 40 1200 30V810C1100 775 980 790 850 805 C650 828 450 780 250 795 C140 803 60 830 0 845Z" fill="var(--teal-band)"/>
</svg>
<div class="abs services-head svc-eyebrow">WHAT WE PROVIDE</div>
<h2 class="abs services-head svc-title">WATER PLUMBING SERVICES</h2>
<p class="abs services-head svc-text">Lorem ipsum dolor sit amet, consectetur adipiscing elit, sed do eiusmod tempor incididunt ut labore et dolore magna aliqua. Ut enim ad minim veniam, quis nostrud exercitation ullamco laboris nisi ut aliquip ex ea commodo.</p>

<div class="svc-item" style="left:166px"><div class="svc-icon active"><svg width="30" height="34" viewBox="0 0 30 34"><path d="M15 2C10 10 5 15 5 22a10 10 0 0 0 20 0C25 15 20 10 15 2z" fill="var(--navy)"/></svg></div>Water Heater<br>Replacement</div>
<div class="svc-sep" style="left:306px"></div>
<div class="svc-item" style="left:310px"><div class="svc-icon"><svg width="30" height="30" viewBox="0 0 30 30" fill="none" stroke="#fff" stroke-width="2"><rect x="8" y="4" width="14" height="18" rx="2"/><circle cx="15" cy="12" r="3"/><path d="M11 22v5M19 22v5"/></svg></div>Tankless Water<br>Heater Installation</div>
<div class="svc-sep" style="left:450px"></div>
<div class="svc-item" style="left:453px"><div class="svc-icon"><svg width="30" height="30" viewBox="0 0 30 30" fill="none" stroke="#fff" stroke-width="2"><path d="M4 16h22v4a5 5 0 0 1-5 5H9a5 5 0 0 1-5-5z"/><path d="M8 16V6a3 3 0 0 1 6 0"/></svg></div>Kitchen and<br>Bath Remodel</div>
<div class="svc-sep" style="left:593px"></div>
<div class="svc-item" style="left:595px"><div class="svc-icon"><svg width="30" height="30" viewBox="0 0 30 30" fill="none" stroke="#fff" stroke-width="2"><path d="M6 6l12 12M14 22l8-8 4 4-8 8z"/></svg></div>Drain Cleaning<br>and Clog Removal</div>
<div class="svc-sep" style="left:736px"></div>
<div class="svc-item" style="left:738px"><div class="svc-icon"><svg width="30" height="30" viewBox="0 0 30 30" fill="none" stroke="#fff" stroke-width="2"><path d="M5 8h14v6H11v10H5z"/><path d="M19 11h6M22 17v6"/></svg></div>Leak repair</div>
<div class="svc-sep" style="left:878px"></div>
<div class="svc-item" style="left:882px"><div class="svc-icon"><svg width="30" height="30" viewBox="0 0 30 30" fill="none" stroke="#fff" stroke-width="2"><path d="M10 6h10M15 6v6M4 14h18v5H4zM22 16h4v8"/></svg></div>Faucet Repair<br>and Replacement</div>
<div class="abs svc-underline"></div>

<h3 class="abs svc-detail-title">Water Heater Replacement</h3>
<p class="abs svc-detail-sub">Need water Plumbing &amp; Drain Cleaning Services?<br>It's all in our name.</p>
<p class="abs svc-detail-text">Lorem ipsum dolor sit amet, consectetur adipiscing elit, sed do eiusmod tempor incididunt ut labore et dolore magna aliqua. Ut enim ad minim veniam, quis nostrud exercitation ullamco laboris nisi ut aliquip ex ea commodo consequat. Duis aute irure dolor in reprehenderit in voluptate velit esse cillum dolore eu fugiat nulla pariatur. Excepteur sint occaecat cupidatat non proident, sunt in culpa qui officia deserunt mollit anim id est laborum. Sed ut perspiciatis unde omnis iste natus error sit.</p>
<div class="btn btn-svc">Request Services</div>
<div class="img-fill" role="img" aria-label="Technician in yellow gloves servicing a wall-mounted water heater" style="left:625px;top:1744px;width:360px;height:318px;background:linear-gradient(135deg,#e9eef2 0%,#c7d0d8 55%,#8b7a5a 100%);border-radius:6px"></div>

<!-- Testimonials -->
<section class="abs testimonials"></section>
<div class="abs center tst-eyebrow">OUR TESTIMONIALS</div>
<div class="abs tst-bar"></div>
<h2 class="abs center tst-title">What Our Client Are saying</h2>
<p class="abs center tst-sub">Lorem ipsum dolor sit amet, consectetur adipiscing sed do eiusmod tempor.</p>

<div class="arrow" style="left:89px"><svg width="20" height="12" viewBox="0 0 20 12" fill="none" stroke="var(--navy)" stroke-width="1.8"><path d="M19 6H2M7 1L2 6l5 5"/></svg></div>
<div class="arrow" style="left:1063px"><svg width="20" height="12" viewBox="0 0 20 12" fill="none" stroke="var(--navy)" stroke-width="1.8"><path d="M1 6h17M13 1l5 5-5 5"/></svg></div>

<div class="tcard" style="left:175px"><div class="quote">&ldquo;</div><p>Lorem ipsum dolor sit amet, consectetur adipiscing elit, sed do eiusmod tempor incididunt ut labore et dolore magna aliqua enim ad minim veniam quis nostrud."</p><div class="stars">★★★★★</div><div class="g"></div><div class="name">Daniel Hartley</div><div class="role">Lorem Ipsum Doler</div></div>
<div class="tcard" style="left:469px"><div class="quote">&ldquo;</div><p>Lorem ipsum dolor sit amet, consectetur adipiscing elit, sed do eiusmod tempor incididunt ut labore et dolore magna aliqua enim ad minim veniam quis nostrud."</p><div class="stars">★★★★★</div><div class="g"></div><div class="name">Daniel Hartley</div><div class="role">Lorem Ipsum Doler</div></div>
<div class="tcard" style="left:765px"><div class="quote">&ldquo;</div><p>Lorem ipsum dolor sit amet, consectetur adipiscing elit, sed do eiusmod tempor incididunt ut labore et dolore magna aliqua enim ad minim veniam quis nostrud."</p><div class="stars">★★★★★</div><div class="g"></div><div class="name">Daniel Hartley</div><div class="role">Lorem Ipsum Doler</div></div>

<!-- Location -->
<div class="abs loc-eyebrow">OUR LOCATION</div>
<h2 class="abs loc-title">AREAS WE PROUDLY SERVE</h2>
<p class="abs loc-text">Lorem ipsum dolor sit amet, consectetur adipiscing elit, sed do eiusmod tempor incididunt ut labore et dolore magna aliqua. Ut enim ad minim veniam, quis nostrud exercitation ate ullamco laboris nisi ut aliquip ex ea commodo consequat.</p>
<div class="abs areas-card">
  <div class="areas-tab active" style="left:12px;width:147px">LOREM IPSUM</div>
  <div class="areas-tab" style="left:190px;width:120px">LOREM IPSUM</div>
  <div class="areas-tab" style="left:330px;width:120px">LOREM IPSUM</div>
  <div class="area" style="left:13px;top:70px"><svg width="9" height="12" viewBox="0 0 9 12"><path d="M4.5 0A4.5 4.5 0 0 0 0 4.5C0 8 4.5 12 4.5 12S9 8 9 4.5A4.5 4.5 0 0 0 4.5 0z" fill="var(--teal)"/><circle cx="4.5" cy="4.5" r="1.6" fill="#fff"/></svg>Bucks County</div>
  <div class="area" style="left:13px;top:101px"><svg width="9" height="12" viewBox="0 0 9 12"><path d="M4.5 0A4.5 4.5 0 0 0 0 4.5C0 8 4.5 12 4.5 12S9 8 9 4.5A4.5 4.5 0 0 0 4.5 0z" fill="var(--teal)"/><circle cx="4.5" cy="4.5" r="1.6" fill="#fff"/></svg>Delaware County</div>
  <div class="area" style="left:13px;top:131px"><svg width="9" height="12" viewBox="0 0 9 12"><path d="M4.5 0A4.5 4.5 0 0 0 0 4.5C0 8 4.5 12 4.5 12S9 8 9 4.5A4.5 4.5 0 0 0 4.5 0z" fill="var(--teal)"/><circle cx="4.5" cy="4.5" r="1.6" fill="#fff"/></svg>Chester County</div>
  <div class="area" style="left:13px;top:162px"><svg width="9" height="12" viewBox="0 0 9 12"><path d="M4.5 0A4.5 4.5 0 0 0 0 4.5C0 8 4.5 12 4.5 12S9 8 9 4.5A4.5 4.5 0 0 0 4.5 0z" fill="var(--teal)"/><circle cx="4.5" cy="4.5" r="1.6" fill="#fff"/></svg>Montgomery County</div>
  <div class="area" style="left:199px;top:70px"><svg width="9" height="12" viewBox="0 0 9 12"><path d="M4.5 0A4.5 4.5 0 0 0 0 4.5C0 8 4.5 12 4.5 12S9 8 9 4.5A4.5 4.5 0 0 0 4.5 0z" fill="var(--teal)"/><circle cx="4.5" cy="4.5" r="1.6" fill="#fff"/></svg>Springfield, PA</div>
  <div class="area" style="left:199px;top:101px"><svg width="9" height="12" viewBox="0 0 9 12"><path d="M4.5 0A4.5 4.5 0 0 0 0 4.5C0 8 4.5 12 4.5 12S9 8 9 4.5A4.5 4.5 0 0 0 4.5 0z" fill="var(--teal)"/><circle cx="4.5" cy="4.5" r="1.6" fill="#fff"/></svg>Elkins Park, PA</div>
  <div class="area" style="left:199px;top:131px"><svg width="9" height="12" viewBox="0 0 9 12"><path d="M4.5 0A4.5 4.5 0 0 0 0 4.5C0 8 4.5 12 4.5 12S9 8 9 4.5A4.5 4.5 0 0 0 4.5 0z" fill="var(--teal)"/><circle cx="4.5" cy="4.5" r="1.6" fill="#fff"/></svg>University City</div>
  <div class="area" style="left:199px;top:162px"><svg width="9" height="12" viewBox="0 0 9 12"><path d="M4.5 0A4.5 4.5 0 0 0 0 4.5C0 8 4.5 12 4.5 12S9 8 9 4.5A4.5 4.5 0 0 0 4.5 0z" fill="var(--teal)"/><circle cx="4.5" cy="4.5" r="1.6" fill="#fff"/></svg>Fishtown</div>
  <div class="area" style="left:335px;top:70px"><svg width="9" height="12" viewBox="0 0 9 12"><path d="M4.5 0A4.5 4.5 0 0 0 0 4.5C0 8 4.5 12 4.5 12S9 8 9 4.5A4.5 4.5 0 0 0 4.5 0z" fill="var(--teal)"/><circle cx="4.5" cy="4.5" r="1.6" fill="#fff"/></svg>Montgomery County</div>
  <div class="area" style="left:335px;top:101px"><svg width="9" height="12" viewBox="0 0 9 12"><path d="M4.5 0A4.5 4.5 0 0 0 0 4.5C0 8 4.5 12 4.5 12S9 8 9 4.5A4.5 4.5 0 0 0 4.5 0z" fill="var(--teal)"/><circle cx="4.5" cy="4.5" r="1.6" fill="#fff"/></svg>Prospect Park, PA</div>
  <div class="area" style="left:335px;top:131px"><svg width="9" height="12" viewBox="0 0 9 12"><path d="M4.5 0A4.5 4.5 0 0 0 0 4.5C0 8 4.5 12 4.5 12S9 8 9 4.5A4.5 4.5 0 0 0 4.5 0z" fill="var(--teal)"/><circle cx="4.5" cy="4.5" r="1.6" fill="#fff"/></svg>Fishtown</div>
  <div class="area" style="left:335px;top:162px"><svg width="9" height="12" viewBox="0 0 9 12"><path d="M4.5 0A4.5 4.5 0 0 0 0 4.5C0 8 4.5 12 4.5 12S9 8 9 4.5A4.5 4.5 0 0 0 4.5 0z" fill="var(--teal)"/><circle cx="4.5" cy="4.5" r="1.6" fill="#fff"/></svg>Philadelphia</div>
</div>
<div class="abs map-circle" role="img" aria-label="Circular street map of the Philadelphia service area with a location pin"></div>

<!-- Contact -->
<div class="abs contact-bg"></div>
<div class="abs footer"></div>
<div class="abs center ct-eyebrow">Clearline Plumbing</div>
<h2 class="abs center ct-title">GET IN TOUCH</h2>
<div class="abs contact-card"></div>
<h3 class="abs ct-heading">Contact Us</h3>
<p class="abs ct-lead">It is a long established fact that a reader will be distracted by the readable content.</p>

<div class="ct-icon" style="top:3482px"><svg width="22" height="22" viewBox="0 0 24 24" fill="none" stroke="#fff" stroke-width="1.8"><path d="M12 2a7 7 0 0 0-7 7c0 5 7 13 7 13s7-8 7-13a7 7 0 0 0-7-7z"/><circle cx="12" cy="9" r="2.5"/></svg></div>
<div class="ct-label" style="top:3478px">Location:</div>
<div class="ct-value" style="top:3500px">Address: Lorem ipsum dolor sit amet, consectetur adipiscing.</div>

<div class="ct-icon" style="top:3569px"><svg width="22" height="22" viewBox="0 0 24 24" fill="none" stroke="#fff" stroke-width="1.8"><rect x="3" y="6" width="18" height="13" rx="1"/><path d="M3 7l9 7 9-7"/></svg></div>
<div class="ct-label" style="top:3573px">Email Address:</div>
<div class="ct-value" style="top:3595px">(101) 555-01-234</div>

<div class="ct-icon" style="top:3656px"><svg width="20" height="20" viewBox="0 0 24 24"><path d="M6.6 10.8a15 15 0 0 0 6.6 6.6l2.2-2.2a1 1 0 0 1 1-.25 11.4 11.4 0 0 0 3.6.57 1 1 0 0 1 1 1V20a1 1 0 0 1-1 1A17 17 0 0 1 3 4a1 1 0 0 1 1-1h3.5a1 1 0 0 1 1 1c0 1.25.2 2.45.57 3.6a1 1 0 0 1-.25 1z" fill="#fff"/></svg></div>
<div class="ct-label" style="top:3659px">Phone Number:</div>
<div class="ct-value" style="top:3681px">info@clearlineplumbing.com</div>

<div class="abs form-box">
  <div class="form-title">SEND US A MESSAGE</div>
  <div class="field" style="top:104px">First Name*</div>
  <div class="field" style="top:152px">Last Name*</div>
  <div class="field" style="top:197px">Email*</div>
  <div class="field" style="top:238px">Subject*</div>
  <div class="field" style="top:300px;padding-bottom:12px">Your message here*</div>
</div>
<div class="btn btn-send">Send Message</div>

<!-- Footer -->
<div class="abs foot-brand">
  <div class="mark"></div>
  <div class="brand-name">CLEARLINE PLUMBING</div>
</div>
<p class="abs foot-about">Need sewer or drain cleaning services? It's all in our name. At Clearline Drain Cleaning &amp; Plumbing, we specialize in Water Plumbing services.</p>

<div class="abs foot-col" style="left:436px;top:3878px">
  <h4>QUICK LINKS</h4>
  <ul><li>Home</li><li>About Us</li><li>Services</li><li>Contact Us</li></ul>
</div>
<div class="abs foot-col" style="left:610px;top:3878px">
  <h4>OUR SERVICES</h4>
  <ul><li>Water heater replacement</li><li>Tankless water heater installation</li><li>Kitchen and bath remodel</li><li>Drain cleaning and clog removal</li><li>Leak repair</li><li>Faucet repair and replacement</li></ul>
</div>
<div class="abs foot-col foot-contact" style="left:864px;top:3878px;width:210px">
  <h4>CONTACT INFO</h4>
  <ul>
    <li><svg width="14" height="16" viewBox="0 0 24 24" fill="none" stroke="var(--teal)" stroke-width="2"><path d="M12 2a7 7 0 0 0-7 7c0 5 7 13 7 13s7-8 7-13a7 7 0 0 0-7-7z"/></svg><span>Address: Lorem ipsum dolor sit amet, consectetur.</span></li>
    <li><svg width="14" height="14" viewBox="0 0 24 24"><path d="M6.6 10.8a15 15 0 0 0 6.6 6.6l2.2-2.2a1 1 0 0 1 1-.25 11.4 11.4 0 0 0 3.6.57 1 1 0 0 1 1 1V20a1 1 0 0 1-1 1A17 17 0 0 1 3 4a1 1 0 0 1 1-1h3.5a1 1 0 0 1 1 1c0 1.25.2 2.45.57 3.6a1 1 0 0 1-.25 1z" fill="var(--teal)"/></svg><span>(101) 555-01-234</span></li>
    <li><svg width="14" height="14" viewBox="0 0 24 24" fill="none" stroke="var(--teal)" stroke-width="2"><rect x="3" y="6" width="18" height="13" rx="1"/><path d="M3 7l9 7 9-7"/></svg><span>info@clearlineplumbing.com</span></li>
  </ul>
</div>
<div class="abs center copyright">© 2023 Clearline Plumbing. All rights reserved</div>

</body>
</html>
```